Italian Grape Importer needs a Wine Label Design

Uva Dorata provides home winemakers and vineyards with ultra-premium frozen wine grapes direct from Italy. Uva Dorata grapes are highly unique, as they are the only wine grapes available worldwide that are 100% Organic and have the prestigious Italian DOCG certification. We have developed a patented process for flash-freezing wine grapes, right after being picked off of our wines in Italy. This ensures unparalleled quality for the most discerning winemakers around the world.
In addition to its expanding line of premium wine grapes, Uva Dorata also imports high-quality winemaking equipment, such as wine vats, pumps, buckets, etc.
We are looking for a professional graphic designer to create a wine label for us for a wine named "Riverbo": a 50/50 blend of Cabernet Sauvignon and Merlot. In Italian, riverbo means "the encounter/meeting". This wine will be used to promote our grapes to potential customers, both home winemakers and professional wineries and vineyards.
The label should be elegant, clean and modern, yet is approachable to our target consumer (target consumer notes below).
Target Markets:
1. Intermediate and advanced home winemakers looking for high-quality wine grapes (and equipment) that is authentically Italian. These consumers typically are affluent but earthy. They often read Cellarcraft Journal – the #1 magazine for home winemaking.
2. Small vineyards that are looking to supplement their inventory with high-quality imported wine grapes.
The label should measure 4" x 6" and include the following information:
Brand Name: Uva Dorata
Uva Dorata Logo
Wine Name: Riverbo
Blend: 50/50 Cabernet Sauvignon/Merlot
Organic, DOCG, Tuscany
Look and Feel:
• Elegant
• Serious
• Modern/Traditional
• Personable but Professional
• Gender Neutral
• Upmarket
I have attached example images to demonstrate the feel that we are looking for. These are just a possible starting point. The expectation is that the label would be professional/polished.
Note:
I've added some wine labels that we've come across that have the feel that we would like for our wine label. We want it to be clean and elegant - think valdren kross, KTR, Lavelle & Boiron. One possible color to be used is Pantone 19-2524 (Dark Purple), or Pantone 19-2428 (Magenta Purple) with silver/grey/black

```html
<!DOCTYPE html>
<html lang="it">
<head>
<meta charset="utf-8">
<title>Riverbo – Uva Dorata</title>
<link rel="stylesheet" href="https://fonts.googleapis.com/css2?family=Kaushan+Script&family=Italianno&family=Playball&display=swap">
<style>
  :root {
    --label-purple: #5b1670;
    --swirl-violet: #6a1ef5;
    --swirl-deep: #3e1360;
    --silver: #bccac0;
  }
  * { margin: 0; padding: 0; box-sizing: border-box; }
  html, body {
    width: 1125px;
    height: 1200px;
    overflow: hidden;
    background: var(--label-purple);
  }
  .label {
    position: relative;
    width: 1125px;
    height: 1200px;
    background: var(--label-purple);
    overflow: hidden;
  }
  .swirl-art {
    position: absolute;
    left: 115px;
    top: 103px;
    width: 892px;
    height: 892px;
  }
  .wine-name {
    position: absolute;
    left: 0;
    top: 20px;
    width: 1125px;
    text-align: center;
    font-family: "Kaushan Script", cursive;
    font-size: 330px;
    line-height: 1;
    color: var(--silver);
    letter-spacing: -4px;
  }
  .brand-name {
    position: absolute;
    left: 0;
    top: 540px;
    width: 1125px;
    text-align: center;
    font-family: "Italianno", cursive;
    font-size: 110px;
    line-height: 1.1;
    color: var(--silver);
  }
  .wine-details {
    position: absolute;
    left: 0;
    top: 1042px;
    width: 1125px;
    text-align: center;
    font-family: "Playball", cursive;
    font-size: 32px;
    line-height: 64px;
    color: var(--silver);
  }
</style>
</head>
<body>
  <main class="label">
    <svg class="swirl-art" viewBox="0 0 892 892" role="img" aria-label="Large violet spiral swirl motif behind the lettering">
      <defs>
        <radialGradient id="swirlTone" cx="50%" cy="50%" r="50%">
          <stop offset="0%" stop-color="#4a1582"/>
          <stop offset="55%" stop-color="#541aa6"/>
          <stop offset="100%" stop-color="#5a1cc4"/>
        </radialGradient>
      </defs>
      <circle cx="446" cy="446" r="446" fill="url(#swirlTone)"/>
    </svg>

    <h1 class="wine-name">Riverbo</h1>
    <p class="brand-name">Uva Dorata</p>

    <p class="wine-details">
      50/50 Cabernet Sauvignon/Merlot<br>
      Organic, DOCG
    </p>
  </main>
</body>
</html>
```